Logo/Stationary for Personal Injury Law Firm

We need a logo for our firm and stationary (letterhead, business cards, envelopes) to feature it. We are a personal injury firm that is branching off and starting on our own. Our firm name is "Halvorsen Law, P.C." We would like to take a more modern approach with the design, but still look professional. Our firm takes a very personal approach with all of our clients.
Updates
Here is the info located in the supported file (if you couldnt access it): 4127 North Birchwood Lane Oklahoma City, Oklahoma 73482 Telephone: (405) 362-8140 Fax: (405) 362-8177 Toll Free: (866) 362-8140 Website: www.HalvorsenLaw.example Email: name@halvorsenlaw.example Attorneys: Garrett Halvorsen – licensed to practice in Oklahoma Dustin Pellow – licensed to practice in Oklahoma Of Counsel Cyrus Ponder – licensed to practice in Texas Stefan Ruokola – licensed to practice in New York
Halvorsen Law, P.C.
I have attached an example of the letterhead from our old firm. The main attorneys (Garrett & Dustin) should come first and the of counsel attorneys should be second because they just assist with cases. But please don't let this example box you in to a certain concept.
Target Market(s)
Potential clients involved in personal injury cases (auto accidents, pharmaceutical litigation, medical malpractice & nursing home negligence).
Industry/Entity Type
Lawyer
Requirements
Must have
- Logo - Firm name "Halvorsen Law, P.C."
- Letterhead - Please see the supporting file containing all the information that needs to be presented.
- Business Card - name, title (attorney/legal assistant), address, telephone, fax, email, website
- Envelope - Logo and address
Should not have
- All of the attorneys are male, so we aren''t interested in any feminine designs.
- Please do not use any scales, gavels or family crest designs.

```html
<!DOCTYPE html>
<html lang="en">
<head>
<meta charset="utf-8">
<title>Halvorsen Law, P.C. — Stationery</title>
<link rel="stylesheet" href="https://fonts.googleapis.com/css2?family=EB+Garamond:wght@400;600&display=swap">
<style>
:root{
  --navy:#023c70;
  --pale:#cfd9e2;
  --paper:#ffffff;
  --ink-bg:#000000;
  --label:#ffffff;
}
*{margin:0;padding:0;box-sizing:border-box}
html,body{width:1200px;height:849px;overflow:hidden;background:var(--ink-bg)}
body{position:relative;font-family:"EB Garamond",Garamond,serif;color:var(--navy)}
.abs{position:absolute}

/* wordmark */
.wordmark{font-family:"EB Garamond",serif;font-weight:400;color:var(--navy);text-align:center;line-height:1.05;letter-spacing:.04em;text-transform:uppercase}
.wordmark.light{color:var(--paper)}

/* contact blocks */
.contact{text-align:right;line-height:1.45;font-size:7.4px;color:var(--navy)}
.contact .firm{font-weight:600;font-size:8.6px}
.contact .gap{height:8px}

/* letterhead */
.letterhead{left:27px;top:29px;width:616px;height:798px;background:var(--paper)}
.letterhead .band{right:0;top:0;width:73px;height:100%}
.letterhead .wordmark{left:36px;top:42px;width:120px;font-size:19px}
.letterhead .contact{right:87px;top:36px;font-size:7.6px;line-height:1.45}

/* business cards */
.card{width:218px;height:129px;overflow:hidden;background:var(--paper);border-radius:0 22px 0 22px}
.card .wordmark{left:0;right:0;top:44px;font-size:17px}
.card.back{background:var(--pale)}
.card.back .side{right:0;top:0;width:93px;height:100%;background:var(--navy)}
.card.back .contact{right:99px;top:19px;font-size:6.2px;line-height:1.52}
.card.back .contact .firm{font-size:7.4px}
.card.back .contact .gap{height:5px}
.card.back .person{left:130px;top:20px;color:var(--paper)}
.person .name{font-size:7.6px;font-weight:600}
.person .role{font-size:4.4px;margin-top:1px}

/* envelope */
.envelope{left:370px;top:362px;width:566px;height:282px}
.envelope .band{right:0;top:0;width:93px;height:100%;background:var(--navy)}
.envelope .body{left:0;top:0;width:519px;height:100%;background:var(--paper);border:1px solid #222;border-right:none;border-top-right-radius:24px}
.envelope .wordmark{left:20px;top:200px;width:104px;font-size:14px}
.envelope .contact{right:136px;top:180px;font-size:6.4px;line-height:1.48}
.envelope .contact .firm{font-size:7.8px}
.envelope .contact .gap{height:7px}

/* labels */
.label{color:var(--label);font-size:10.5px;white-space:nowrap}

/* showcase marks */
.showcase{width:150px;font-size:24px}
</style>
</head>
<body>

<section class="letterhead abs" aria-label="Letterhead">
  <svg class="band abs" viewBox="0 0 73 798" preserveAspectRatio="none" aria-hidden="true">
    <rect width="73" height="798" fill="#023c70"/>
    <rect x="11" width="6" height="798" fill="#fff"/>
    <rect x="24" width="6" height="798" fill="#fff"/>
    <rect x="37" width="6" height="798" fill="#fff"/>
  </svg>
  <div class="wordmark abs">Halvorsen<br>Law P.C.</div>
  <div class="contact abs">
    <div class="firm">Halvorsen Law, P.C.</div>
    <div>4127 North Birchwood Lane</div>
    <div>Oklahoma City, Oklahoma 73482</div>
    <div class="gap"></div>
    <div>Telephone: (405) 362-8140</div>
    <div>Fax: (405) 362-8177</div>
    <div>Toll Free: (866) 362-8140</div>
    <div>Website: www.HalvorsenLaw.example</div>
  </div>
</section>

<div class="card abs" style="left:690px;top:42px"><div class="wordmark abs">Halvorsen<br>Law P.C.</div></div>
<div class="card abs" style="left:690px;top:181px"><div class="wordmark abs">Halvorsen<br>Law P.C.</div></div>

<div class="card back abs" style="left:927px;top:41px">
  <div class="side abs"></div>
  <div class="contact abs">
    <div class="firm">Halvorsen Law, P.C.</div>
    <div>4127 North Birchwood Lane</div>
    <div>Oklahoma City, Oklahoma 73482</div>
    <div class="gap"></div>
    <div>Telephone: (405) 362-8140</div>
    <div>Fax: (405) 362-8177</div>
    <div>Toll Free: (866) 362-8140</div>
    <div>Website: www.HalvorsenLaw.example</div>
    <div>Email: garretthalvorsen@halvorsenlaw.example</div>
  </div>
  <div class="person abs"><div class="name">Garrett Halvorsen</div><div class="role">licensed to practice in Oklahoma</div></div>
</div>

<div class="card back abs" style="left:927px;top:181px">
  <div class="side abs"></div>
  <div class="contact abs">
    <div class="firm">Halvorsen Law, P.C.</div>
    <div>4127 North Birchwood Lane</div>
    <div>Oklahoma City, Oklahoma 73482</div>
    <div class="gap"></div>
    <div>Telephone: (405) 362-8140</div>
    <div>Fax: (405) 362-8177</div>
    <div>Toll Free: (866) 362-8140</div>
    <div>Website: www.HalvorsenLaw.example</div>
    <div>Email: dustinpellow@halvorsenlaw.example</div>
  </div>
  <div class="person abs"><div class="name">Dustin Pellow</div><div class="role">– licensed to practice in Oklahoma</div></div>
</div>

<div class="label abs" style="left:714px;top:318px">Business cards front design</div>
<div class="label abs" style="left:926px;top:318px">Business cards back design</div>

<section class="envelope abs" aria-label="Envelope">
  <div class="band abs"></div>
  <svg class="abs" style="right:0;top:0" width="93" height="282" viewBox="0 0 93 282" aria-hidden="true">
    <rect x="53" y="40" width="4" height="188" fill="#fff"/>
    <rect x="63" y="40" width="4" height="188" fill="#fff"/>
    <rect x="73" y="40" width="4" height="188" fill="#fff"/>
  </svg>
  <div class="body abs"></div>
  <div class="wordmark abs" style="top:38px">Halvorsen<br>Law P.C.</div>
  <div class="contact abs">
    <div class="firm">Halvorsen Law, P.C.</div>
    <div>4127 North Birchwood Lane</div>
    <div>Oklahoma City, Oklahoma 73482</div>
    <div class="gap"></div>
    <div>Telephone: (405) 362-8140</div>
    <div>Fax: (405) 362-8177</div>
    <div>Toll Free: (866) 362-8140</div>
    <div>Website: www.HalvorsenLaw.example</div>
  </div>
</section>

<div class="label abs" style="left:850px;top:662px">Envelope design</div>
<div class="label abs" style="left:661px;top:785px">Letterhead design</div>

<div class="wordmark light showcase abs" style="left:999px;top:530px">Halvorsen<br>Law P.C.</div>
<div class="wordmark showcase abs" style="left:999px;top:712px">Halvorsen<br>Law P.C.</div>

</body>
</html>
```